Website for Solar Renewable Company

We Driftova Solar, are in need on a new website design. We design , manufacture and install floating solar plants. These plants are installed on reservoir , lakes and captive reservoir. We would like to build a professional website which shows the technical competency of our company as our product is highly technical .

Videos our projects
https://www.clipharbor.example/watch?v=Qm3rTz8LwKa
https://www.clipharbor.example/watch?v=Vn7pXe2HdYo&t=115s
https://www.clipharbor.example/watch?v=Rb4s_9GmUWq&t=4s

Please see reference competitor websites
https://moulin-de-brume.example/
https://en.brightvalemotive.example/
https://qz-raftgrid.example/

Tabs Needed
- About
- Team
- Solutions
- Projects
- News Update
- Contact

These are not certain - you can change the tabs if you want

Target Market(s)

Developer and EPC companies

Industry/Entity Type

Solar , Renewable Energy, Power

Coding

Coded - Design and coding required

Number of Pages Required

5+ page

Colors
0094D4
00A9DD
6FCCEA
C7EBF8
E9F6FB

Requirements
Nice to have
• Videos

```html
<!DOCTYPE html>
<html lang="en">
<head>
<meta charset="utf-8">
<title>Driftova Solar — Floating Solar Plants</title>
<link rel="stylesheet" href="https://fonts.googleapis.com/css2?family=Ubuntu:wght@400;500;700&family=Raleway:wght@400;500;600&display=swap">
<style>
:root{
  --navy:#1c3a78;
  --navy-dark:#15306a;
  --sun:#f7b614;
  --sun-deep:#e3a40c;
  --sky:#1596d6;
  --sky-2:#00a9dd;
  --sky-3:#6fccea;
  --pale:#e9f6fb;
  --ink:#222;
  --grey:#555;
  --footer:#1b1b1b;
}
*{box-sizing:border-box;margin:0;padding:0}
html,body{width:1200px;height:3897px;overflow:hidden}
body{position:relative;font-family:"Raleway",sans-serif;color:var(--ink);background:#fff}
.abs{position:absolute}
h1,h2,h3,h4{font-family:"Ubuntu",sans-serif;font-weight:500}

/* header */
.topbar{left:0;top:0;width:1200px;height:96px;border-top:4px solid var(--sun);background:#fff}
.brand{left:98px;top:26px;font-family:"Ubuntu",sans-serif;font-weight:700;font-size:30px;color:var(--navy);letter-spacing:1px;display:flex;align-items:center;gap:10px}
.brand .dot{width:14px;height:14px;background:var(--sun);border-radius:50%}
.contact{display:flex;align-items:center;gap:14px;top:28px}
.contact .ico{width:38px;height:38px;border-radius:50%;background:var(--sun);display:flex;align-items:center;justify-content:center}
.contact small{display:block;font-size:11px;font-weight:600;color:#333;letter-spacing:.5px}
.contact span{font-size:14px;color:#333}
.nav{left:0;top:96px;width:1200px;height:66px;background:var(--navy)}
.nav ul{list-style:none;display:flex;gap:30px;position:absolute;left:98px;top:21px}
.nav a{color:#fff;text-decoration:none;font-family:"Ubuntu",sans-serif;font-size:18px}
.consult{left:890px;top:96px;width:211px;height:66px;background:var(--sun);color:#fff;font-family:"Ubuntu",sans-serif;font-weight:500;font-size:20px;display:flex;align-items:center;justify-content:flex-end;padding-right:16px;clip-path:polygon(12% 0,100% 0,100% 100%,0 100%)}

/* hero */
.hero{left:0;top:162px;width:1200px;height:664px;background:linear-gradient(180deg,#9fb2c2 0%,#5b8fb8 35%,#1f8fd0 75%,#1596d6 100%)}
.play{left:350px;top:363px;width:90px;height:90px;border-radius:50%;background:var(--sun);display:flex;align-items:center;justify-content:center;box-shadow:0 0 0 10px rgba(247,182,20,.25)}
.hero-title{left:626px;top:272px;color:#fff}
.hero-title .w{font-family:"Ubuntu",sans-serif;font-size:44px;font-weight:400;letter-spacing:1px}
.hero-title .big{font-family:"Ubuntu",sans-serif;font-size:92px;font-weight:500;line-height:1.12}
.dots{left:1146px;top:446px;display:flex;flex-direction:column;gap:10px}
.dots i{width:16px;height:16px;border-radius:50%;background:var(--sun);border:3px solid rgba(255,255,255,.6)}
.dots i.off{background:transparent;border:2px solid #fff}

/* section heading */
.sec-title{font-family:"Ubuntu",sans-serif;font-weight:500;font-size:33px;color:var(--navy);display:flex;align-items:center;gap:22px;left:0;width:1200px;justify-content:center}
.sec-title::before,.sec-title::after{content:"";width:82px;height:2px;background:var(--sun)}
.sec-title.light{color:#fff}

/* about */
.about-h{left:116px;top:912px;font-size:35px;color:var(--navy);display:flex;align-items:center;gap:16px}
.about-h::after{content:"";width:72px;height:2px;background:var(--sun)}
.about-name{left:110px;top:966px;font-family:"Ubuntu",sans-serif;font-weight:700;font-size:56px;color:var(--sun);letter-spacing:1px}
.about-p{left:116px;width:440px;font-size:16px;line-height:26px;color:#333}
.learn{left:104px;top:1272px;width:200px;height:54px;background:var(--sun);color:#fff;font-family:"Ubuntu",sans-serif;font-size:18px;display:flex;align-items:center;justify-content:center;clip-path:polygon(8% 0,100% 0,92% 100%,0 100%)}
.about-tint{left:600px;top:980px;width:200px;height:300px;background:linear-gradient(160deg,#f1f3f6,#e4e8ee);clip-path:polygon(30% 0,100% 0,70% 100%,0 100%)}
.about-img{left:837px;top:920px;width:363px;height:404px;background:linear-gradient(180deg,#c6cfd4 0%,#8c9aa4 45%,#3a4f86 100%)}

/* services */
.band-yellow{left:0;top:1701px;width:1200px;height:791px;background:linear-gradient(180deg,#e9ad1c 0%,#d89a17 60%,#dca01b 100%)}
.svc{width:320px;height:428px;top:1475px;background:var(--navy);color:#fff}
.svc .ph{height:225px}
.svc h3{font-size:21px;margin:24px 20px 10px}
.svc p{font-size:15px;line-height:22px;margin:0 20px;font-family:"Ubuntu",sans-serif;font-weight:400}
.svc .go{position:absolute;right:0;bottom:0;width:68px;height:46px;background:var(--sun);display:flex;align-items:center;justify-content:center}
.svc.active{background:#fff;color:var(--navy);box-shadow:0 6px 18px rgba(0,0,0,.15)}
.svc.active p{color:#2a5aa8}
.arrow-btn{width:46px;height:46px;border-radius:50%;background:#fff;display:flex;align-items:center;justify-content:center;box-shadow:0 2px 6px rgba(0,0,0,.2)}

/* projects */
.proj{top:2041px;width:253px;height:381px;border-radius:8px;overflow:hidden;background:linear-gradient(180deg,#b9c4cc 0%,#5a7090 45%,#243a5e 100%)}
.proj h4{position:absolute;left:19px;bottom:16px;color:#fff;font-size:21px;line-height:26px;font-weight:500}

/* news */
.news{top:2634px;width:310px;height:342px;background:#fff;box-shadow:0 3px 14px rgba(0,0,0,.13)}
.news .ph{height:178px}
.news .tag{position:absolute;left:42px;top:156px;width:226px;height:44px;background:#fff;border-radius:6px 6px 0 0;font-family:"Ubuntu",sans-serif;font-size:16px;display:flex;align-items:center;justify-content:center;color:#222}
.news p{margin:34px 18px 0;text-align:center;font-size:14px;line-height:26px;color:#555}
.news .go{position:absolute;right:0;bottom:0;width:70px;height:42px;background:var(--sun);display:flex;align-items:center;justify-content:center}

/* team */
.team{left:0;top:3055px;width:1200px;height:428px;background:linear-gradient(180deg,#1598d8 0%,#0f8ccc 100%)}
.avatar{width:154px;height:154px;border-radius:50%;border:2px dashed #fff;padding:6px}
.avatar div{width:100%;height:100%;border-radius:50%;background:linear-gradient(180deg,#dbe6ea,#8fb4c7)}
.member h4{color:#fff;font-size:21px;margin-bottom:12px}
.member p{color:#fff;font-size:14px;line-height:24px;width:330px}

/* footer */
.footer{left:0;top:3483px;width:1200px;height:414px;background:var(--footer);color:#fff}
.f-brand{left:110px;top:116px;font-family:"Ubuntu",sans-serif;font-weight:700;font-size:32px;color:var(--sky);display:flex;align-items:center;gap:12px}
.f-brand .dot{width:14px;height:14px;background:var(--sky);border-radius:50%}
.f-about{left:118px;top:210px;width:340px;font-size:17px;line-height:28px}
.f-col h4{font-size:20px;margin-bottom:22px}
.f-col ul{list-style:none}
.f-col li{font-size:16px;line-height:28px;padding-left:24px;position:relative}
.f-col li::before{content:"›";position:absolute;left:0;font-size:18px}
.f-col.small li{font-size:15px;line-height:25.5px;padding-left:16px}
.social{display:flex;gap:12px}
.social i{width:30px;height:30px;border:2px solid #fff;border-radius:50%}
.rule{left:108px;top:334px;width:980px;height:1px;background:#777}
.copy{left:0;top:358px;width:1200px;text-align:center;font-size:17px}
</style>
</head>
<body>

<header>
  <div class="abs topbar">
    <div class="abs brand"><span class="dot"></span>DRIFTOVA SOLAR</div>
    <div class="abs contact" style="left:572px">
      <div class="ico"><svg width="18" height="14" viewBox="0 0 18 14"><rect x="1" y="1" width="16" height="12" rx="1.5" fill="none" stroke="#fff" stroke-width="1.6"/><path d="M1 2l8 6 8-6" fill="none" stroke="#fff" stroke-width="1.6"/></svg></div>
      <div><small>CONTACT MAIL</small><span>info@driftovasolar.example</span></div>
    </div>
    <div class="abs contact" style="left:830px">
      <div class="ico"><svg width="14" height="18" viewBox="0 0 14 18"><path d="M7 17s6-6.5 6-10.5A6 6 0 0 0 1 6.5C1 10.5 7 17 7 17z" fill="#fff"/><circle cx="7" cy="6.5" r="2.2" fill="var(--sun)"/></svg></div>
      <div><small>OUR LOCATION</small><span>125 Lorem ipsum dolor sit amet</span></div>
    </div>
  </div>
  <nav class="abs nav">
    <ul>
      <li><a href="#">Home</a></li><li><a href="#">About</a></li><li><a href="#">Team</a></li><li><a href="#">Solutions</a></li><li><a href="#">Projects</a></li><li><a href="#">News Update</a></li><li><a href="#">Contact</a></li>
    </ul>
  </nav>
  <div class="abs consult">Consultation</div>
</header>

<section class="abs hero" role="img" aria-label="Aerial photo of a floating solar plant on a reservoir with a power station in the distance"></section>
<div class="abs play"><svg width="30" height="34" viewBox="0 0 30 34"><path d="M3 2l25 15L3 32z" fill="#fff"/></svg></div>
<div class="abs hero-title">
  <div class="w">WELCOME TO</div>
  <div class="big">DRIFTOVA<br>SOLAR</div>
</div>
<div class="abs dots"><i></i><i></i><i></i><i class="off"></i></div>

<section>
  <h2 class="abs about-h">About Us</h2>
  <div class="abs about-name">DRIFTOVA SOLAR</div>
  <p class="abs about-p" style="top:1059px">Lorem Ipsum has been the industry's standard dummy teext ever since the 1500s, when an unknown printer took ab galley of type and scrambled it to make.</p>
  <p class="abs about-p" style="top:1150px">Lorem Ipsum has been the industry's standard dummy teext ever since the 1500s, when an unknown printer took ab galley of type and scrambled it to make.</p>
  <div class="abs learn">Learn More</div>
  <div class="abs about-tint"></div>
  <div class="abs about-img" role="img" aria-label="Photo of a technician assembling floating solar panels on site"></div>
</section>

<h2 class="abs sec-title" style="top:1399px">Our Services</h2>
<div class="abs band-yellow" role="img" aria-label="Warm golden map backdrop of project regions"></div>

<article class="abs svc" style="left:98px">
  <div class="ph" role="img" aria-label="Photo of a large floating solar array" style="background:linear-gradient(180deg,#c5ccd3,#4a5e86)"></div>
  <h3>Designing</h3>
  <p>Lorem ipsum dolor sit amet, consectetur adipiscing elit, sed do eiusmod tempor incididunt ut labore et…</p>
  <div class="go"><svg width="44" height="12" viewBox="0 0 44 12"><path d="M0 6h40M34 1l6 5-6 5" stroke="#fff" stroke-width="2.4" fill="none"/></svg></div>
</article>
<article class="abs svc active" style="left:440px">
  <div class="ph" role="img" aria-label="Photo of solar modules being assembled under a canopy" style="background:linear-gradient(180deg,#3f9a8e,#7d8ea0 50%,#2f4f9a)"></div>
  <h3>Site Survey &amp; Analysis</h3>
  <p>Lorem ipsum dolor sit amet, consectetur adipiscing elit, sed do eiusmod tempor incididunt ut labore et…</p>
  <div class="go"><svg width="44" height="12" viewBox="0 0 44 12"><path d="M0 6h40M34 1l6 5-6 5" stroke="#fff" stroke-width="2.4" fill="none"/></svg></div>
</article>
<article class="abs svc" style="left:784px">
  <div class="ph" role="img" aria-label="Photo of a floater supply gantry by a lake" style="background:linear-gradient(180deg,#7fb3e0,#b4c4cc 60%,#5b6f80)"></div>
  <h3>Floater Supply</h3>
  <p>Lorem ipsum dolor sit amet, consectetur adipiscing elit, sed do eiusmod tempor incididunt ut labore et…</p>
  <div class="go"><svg width="44" height="12" viewBox="0 0 44 12"><path d="M0 6h40M34 1l6 5-6 5" stroke="#fff" stroke-width="2.4" fill="none"/></svg></div>
</article>
<div class="abs arrow-btn" style="left:36px;top:1677px"><svg width="12" height="18" viewBox="0 0 12 18"><path d="M10 1L2 9l8 8" stroke="var(--navy)" stroke-width="2" fill="none"/></svg></div>
<div class="abs arrow-btn" style="left:1116px;top:1677px"><svg width="12" height="18" viewBox="0 0 12 18"><path d="M2 1l8 8-8 8" stroke="var(--navy)" stroke-width="2" fill="none"/></svg></div>

<h2 class="abs sec-title light" style="top:1964px">Our Projects</h2>
<div class="abs proj" style="left:133px" role="img" aria-label="Photo of a floating solar project"><h4>Kestral/Vardon<br>Harlow Basin</h4></div>
<div class="abs proj" style="left:415px" role="img" aria-label="Photo of a floating solar project"><h4>Kestral/Vardon<br>Tarrow Lake</h4></div>
<div class="abs proj" style="left:696px" role="img" aria-label="Photo of a floating solar project"><h4>Kestral/Vardon<br>Fenmere</h4></div>
<div class="abs proj" style="left:979px;border-radius:8px 0 0 8px" role="img" aria-label="Photo of a floating solar project"><h4>Kestral/Holmcrest<br>Ostral Reach</h4></div>
<div class="abs arrow-btn" style="left:112px;top:2207px"><svg width="12" height="18" viewBox="0 0 12 18"><path d="M10 1L2 9l8 8" stroke="var(--navy)" stroke-width="2" fill="none"/></svg></div>
<div class="abs arrow-btn" style="left:1116px;top:2207px"><svg width="12" height="18" viewBox="0 0 12 18"><path d="M2 1l8 8-8 8" stroke="var(--navy)" stroke-width="2" fill="none"/></svg></div>

<h2 class="abs sec-title" style="top:2560px">News Update</h2>
<article class="abs news" style="left:100px">
  <div class="ph" role="img" aria-label="Photo of a floating solar plant on a lake" style="background:linear-gradient(180deg,#9fb4bf,#4f6b8c)"></div>
  <div class="tag">SED UT PERSPICIATIS</div>
  <p>Lorem ipsum dolor sit amet, consectetur adipiscing elit, sed do eiusmod tempor incididunt ut labore et dolore magna</p>
  <div class="go"><svg width="32" height="12" viewBox="0 0 32 12"><path d="M0 6h28M22 1l6 5-6 5" stroke="#222" stroke-width="2.4" fill="none"/></svg></div>
</article>
<article class="abs news" style="left:445px">
  <div class="ph" role="img" aria-label="Photo of an installer working on a rooftop solar panel" style="background:linear-gradient(180deg,#7fc0ec,#4c77b2)"></div>
  <div class="tag">SED UT PERSPICIATIS</div>
  <p>Lorem ipsum dolor sit amet, consectetur adipiscing elit, sed do eiusmod tempor incididunt ut labore et dolore magna</p>
  <div class="go"><svg width="32" height="12" viewBox="0 0 32 12"><path d="M0 6h28M22 1l6 5-6 5" stroke="#222" stroke-width="2.4" fill="none"/></svg></div>
</article>
<article class="abs news" style="left:791px">
  <div class="ph" role="img" aria-label="Photo of solar panels on a pond at sunset" style="background:linear-gradient(180deg,#e8c46a,#7fa35a 55%,#3f5f8a)"></div>
  <div class="tag">SED UT PERSPICIATIS</div>
  <p>Lorem ipsum dolor sit amet, consectetur adipiscing elit, sed do eiusmod tempor incididunt ut labore et dolore magna</p>
  <div class="go"><svg width="32" height="12" viewBox="0 0 32 12"><path d="M0 6h28M22 1l6 5-6 5" stroke="#222" stroke-width="2.4" fill="none"/></svg></div>
</article>

<section class="abs team"></section>
<h2 class="abs sec-title light" style="top:3124px">Our Team</h2>
<div class="abs avatar" style="left:99px;top:3221px"><div role="img" aria-label="Portrait of a team member in a hard hat"></div></div>
<div class="abs member" style="left:270px;top:3218px">
  <h4>Jhone Deo</h4>
  <p>Lorem ipsum dolor sit amet, consectetur adipiscing elit, sed do eiusmod tempor incididunt ut labore et dolore magna aliqua. Ut enim ad minim veniam, quis nostrud exercitation ullamco laboris nisi ut aliquip ex ea commodo consequat.</p>
</div>
<div class="abs avatar" style="left:607px;top:3221px"><div role="img" aria-label="Portrait of a team member in a safety vest"></div></div>
<div class="abs member" style="left:792px;top:3218px">
  <h4>Jhone Deo</h4>
  <p>Lorem ipsum dolor sit amet, consectetur adipiscing elit, sed do eiusmod tempor incididunt ut labore et dolore magna aliqua. Ut enim ad minim veniam, quis nostrud exercitation ullamco laboris nisi ut aliquip ex ea commodo consequat.</p>
</div>

<footer class="abs footer">
  <div class="abs f-brand"><span class="dot"></span>DRIFTOVA SOLAR</div>
  <p class="abs f-about">Lorem ipsum dolor sit amet, consectetur adipiscing elit, sed do eiusmod tempor incididunt ut labore et dolore magna aliqua.</p>
  <div class="abs f-col" style="left:490px;top:48px">
    <h4>Quick Link</h4>
    <ul><li>Home</li><li>About</li><li>Team</li><li>Solutions</li><li>Projects</li><li>News Update</li><li>Contact</li></ul>
  </div>
  <div class="abs f-col small" style="left:705px;top:48px">
    <h4>Help Link</h4>
    <ul><li>Terms&amp;condtions</li><li>Privacy Policy</li><li>About Us</li><li>Support</li></ul>
    <h4 style="margin:32px 0 14px">Social Media</h4>
    <div class="social"><i></i><i></i><i></i></div>
  </div>
  <div class="abs f-col small" style="left:888px;top:48px;width:230px">
    <h4>Services</h4>
    <ul><li>Designing</li><li>Site Survey &amp; Analysis</li><li>Floater Supply</li><li>Installation Supervision</li><li>Mooring and Anchoring Designing</li><li>Installation of Mooring &amp; Anchoring</li></ul>
  </div>
  <div class="abs rule"></div>
  <div class="abs copy">© copyrights 2022 Driftova Solar | &nbsp;All Rights Reserved</div>
</footer>

</body>
</html>
```